Etiketten-Design für Nahrungsergänzungsmittel
Zielgruppe
Die Firma vertreibt Nahrungsergänzungsmittel, gesunde Lebensmittel, Lifestyle und Wellnessprodukte. Dies vor allem im Fitness und Sport Bereich. Die Marke und das entsprechende Logo sollen auf eine jüngere Zielgruppe 25+ ausgerichtet sein. Personen die für Ihren Körper und Gesundheit Sport treiben und zusätzlich Unterstützung benötigen. Die Produkte werden über Pictoloop durch eine Fitnesstrainerin beworben, und hauptsächlich über Varuno vertrieben. Produkte sind z. B. Produkte zur Ausdauersteigerung, verbesserte Konzentration, Schlaf, Stressbewältigung. Protein Shakes oder Vitamine für Veganer. No gos, Diät Produkte 5kg in 3 Tagen, Potenzsteigerung, Brustvergrößerung oder ähnliches.
Aufgabenstellung
Das Etikett wird auf einen wiederverschließbaren schwarz matten Kraftpapier Beutel im Format 28x20cm aufgebracht. Der Beutel und auch das Etikett sind kompostierbar, sieht aber beides hochwertig aus. Das Produkt ist ein veganes Proteinpulver zum anrühren mit Wasser oder Milchalternative. Einen ersten Entwurf habe ich hochgeladen.

```html
<!DOCTYPE html>
<html lang="de">
<head>
<meta charset="utf-8">
<title>ELVA – Veganer Protein Shake Etikett</title>
<link href="https://fonts.googleapis.com/css2?family=Poppins:wght@400;500;600;700&family=Montserrat:ital,wght@1,900&display=swap" rel="stylesheet">
<style>
  :root{
    --bg:#2b2b2b;
    --frame:#f2f2f2;
    --label-dark:#1d1d1d;
    --label-mid:#2a2a2a;
    --teal:#12a39a;
    --cell:#474747;
    --text:#ffffff;
  }
  *{box-sizing:border-box;margin:0;padding:0}
  html,body{width:1178px;height:1200px;overflow:hidden;background:var(--bg)}
  body{font-family:"Poppins",sans-serif;color:var(--text);position:relative}
  .label{
    position:absolute;top:240px;width:520px;height:720px;
    border:8px solid var(--frame);border-radius:22px;overflow:hidden;
    background:var(--label-dark);
  }
  .label--front{left:57px}
  .label--back{left:601px}
  .label__bg{position:absolute;inset:0;width:100%;height:100%}
  /* front */
  .brand{position:absolute;left:0;right:0;top:150px;text-align:center}
  .brand__mark{width:54px;height:54px;border-radius:50%;background:var(--teal);margin:0 auto 22px}
  .brand__name{font-family:"Poppins",sans-serif;font-weight:600;font-size:46px;letter-spacing:3px;color:var(--text)}
  .product-title{
    position:absolute;left:100px;top:390px;transform:rotate(-9deg);transform-origin:left top;
    font-family:"Montserrat",sans-serif;font-style:italic;font-weight:900;line-height:.98;
  }
  .product-title span{display:block}
  .product-title .t1{color:var(--teal);font-size:62px;margin-left:14px}
  .product-title .t2{font-size:64px}
  .product-title .t3{font-size:64px;margin-left:38px}
  /* back */
  .back__content{position:absolute;left:28px;top:46px;width:444px;font-size:10.2px;line-height:1.35}
  .intro strong{font-weight:600}
  .intro{margin-bottom:10px}
  table{border-collapse:separate;border-spacing:4px 2px;margin-left:-4px;width:calc(100% + 8px)}
  td,th{text-align:center;font-weight:400;padding:2px 3px;font-size:10.2px}
  th{background:var(--cell);font-weight:600}
  .row--alt td{background:var(--cell)}
  .nutrition td:nth-child(1){width:43%}
  .nutrition td:nth-child(2){width:30%}
  .amino{margin-top:12px}
  .amino td.val{width:9%}
  .amino td.name{width:22%}
  .usage{margin-top:20px;width:200px}
  .usage strong,.company strong{font-weight:600}
  .company{position:absolute;left:28px;top:560px;font-size:10.2px;line-height:1.3}
  .social{position:absolute;left:176px;top:572px;width:135px;text-align:right;font-size:8px;line-height:1.25}
  .social__lead{color:var(--teal);font-weight:600}
  .social__handle{font-weight:600;font-size:10.2px;margin-top:4px;display:flex;justify-content:flex-end;align-items:center;gap:3px}
  .social__handle i{width:9px;height:9px;border-radius:50%;background:var(--teal);display:inline-block}
  .trainer-photo{position:absolute;left:332px;top:484px;width:130px;height:220px;border-radius:60px 60px 0 0;
    background:linear-gradient(180deg,#d8b99f 0%,#9a7d6c 30%,#4b5866 55%,#202022 100%)}
</style>
</head>
<body>

<section class="label label--front">
  <svg class="label__bg" viewBox="0 0 504 704" preserveAspectRatio="none" aria-hidden="true">
    <polygon points="0,0 190,0 0,38" fill="var(--teal)"/>
    <polygon points="0,360 504,285 504,704 0,704" fill="var(--label-mid)"/>
    <polygon points="300,320 504,288 504,300 330,322" fill="var(--teal)"/>
    <polygon points="0,655 504,565 504,704 0,704" fill="var(--teal)"/>
    <polygon points="0,645 200,612 0,640" fill="var(--teal)"/>
  </svg>
  <div class="brand">
    <div class="brand__mark"></div>
    <div class="brand__name">ELVA</div>
  </div>
  <h1 class="product-title">
    <span class="t1">VEGANER</span>
    <span class="t2">PROTEIN</span>
    <span class="t3">SHAKE</span>
  </h1>
</section>

<section class="label label--back">
  <svg class="label__bg" viewBox="0 0 504 704" preserveAspectRatio="none" aria-hidden="true">
    <polygon points="0,700 504,600 504,704 0,704" fill="var(--teal)"/>
    <polygon points="0,690 180,660 0,686" fill="var(--teal)"/>
  </svg>
  <div class="back__content">
    <p class="intro"><strong>Getränkepulver zur Herstellung eines veganen Eiweißgetränkes mit Süßungs­mittel - Geschmacksrichtung Vanille</strong><br>
    Zutaten: Eiweißmischung (93%) (Erbseneiweiß, Reiseiweiß, Hanfsamenpulver, Bio Kürbiskerneiweiß), Aroma, Verdickungsmittel: Xanthan, Kokosnussmilchpulver, Süßungsmittel: Sucralose</p>

    <table class="nutrition">
      <tr><th>Nahrwertangaben pro</th><th>100g</th><th>Portion = 30g</th></tr>
      <tr><td>Energie</td><td>1.694 kJ /<br>401 kcal</td><td>508 kJ /<br>120 kcal</td></tr>
      <tr class="row--alt"><td>Fett</td><td>8,3 g</td><td>2,5 g</td></tr>
      <tr><td>- davon gesättigte Fettsäuren</td><td>2,2 g</td><td>0,7 g</td></tr>
      <tr class="row--alt"><td>Kohlenhydrate</td><td>4,0 g</td><td>1,2 g</td></tr>
      <tr><td>- davon Zucker</td><td>1,2 g</td><td>0,4 g</td></tr>
      <tr class="row--alt"><td>Ballaststoffe</td><td>4,4 g</td><td>1,3 g</td></tr>
      <tr><td>Eiweiß</td><td>75,3 g</td><td>22,6 g</td></tr>
      <tr class="row--alt"><td>Salz</td><td>2,15 g</td><td>0,64 g</td></tr>
    </table>

    <table class="amino">
      <tr><th colspan="6">Aminosäurenprofil pro 100g Eweiß</th></tr>
      <tr><td class="name">Isoleucin</td><td class="val">4,4 g</td><td class="name">Tryptophan</td><td class="val">1,1 g</td><td class="name">Alanin</td><td class="val">8,9 g</td></tr>
      <tr class="row--alt"><td>Leucin</td><td>8,4 g</td><td>Valin</td><td>5,3 g</td><td>Asparaginsäure</td><td>11,1 g</td></tr>
      <tr><td>Lysin</td><td>6,7 g</td><td>Histidin</td><td>2,5 g</td><td>Glutaminsäure</td><td>17,2 g</td></tr>
      <tr class="row--alt"><td>Methionin</td><td>1,4 g</td><td>Arginin</td><td>8,9 g</td><td>Glycin</td><td>4,2 g</td></tr>
      <tr><td>Phenylalanin</td><td>5,5 g</td><td>Tyrosin</td><td>3,8 g</td><td>Prolin</td><td>4,4 g</td></tr>
      <tr class="row--alt"><td>Threonin</td><td>3,7 g</td><td>Cystein</td><td>1,4 g</td><td>Serin</td><td>5,1 g</td></tr>
    </table>

    <p class="usage"><strong>Verzehrempfehlung:</strong> 30 g Pulver <strong>in 300 ml Wasser lösen;</strong><br>Das Produkt ist kühl, trocken und dunkel zu lagern.</p>
  </div>

  <div class="company">
    <strong>ELVAUG</strong><br>
    Lindenhofweg 12<br>
    74912 Birkenau<br>
    info@elvabyelva.de<br>
    Inhalt: 600g Eiweißpulver für 20 Shakes<br>
    Mindestens haltbar bis Ende:<br>
    08/2023; Losnummer: 977109
  </div>

  <div class="social">
    <div class="social__lead">Besucht uns auch auf Pictoloop<br>Liebe Grüße Elva</div>
    <div class="social__handle"><i></i>elvabyelva</div>
  </div>

  <div class="trainer-photo" role="img" aria-label="Foto der Fitnesstrainerin mit verschränkten Armen in Sportkleidung"></div>
</section>

</body>
</html>
```